Colon Cancer Fundraiser Fall 2015

We need a flier design for a fundraiser in September. The event is in our hometown. It is an informal dinner, silent auction, and live band. Family Friendly.

www.brightpathwaynfp.org

Marlow Veterans Hall
September 26 3pm - 10pm
Bean Bag Tournament @ 4pm
Band @ 7 Band Name: Velvet Orchard

Industry/Entity Type

Event

Font styles to use
Sans Serif

Requirements
Must have
• www.brightpathwaynfp.org
• Marlow Veterans Hall
• September 26 3pm - 10pm
• Bean Bag Tournament @ 4pm
• Band @ 7 Band Name: Velvet Orchard
• Contact: Brenda 708-555-0193 brenda@brightpathwaynfp.org

```html
<!DOCTYPE html>
<html lang="en">
<head>
<meta charset="utf-8">
<title>Bright Pathway, NFP – Colon Cancer Fundraiser Fall 2015</title>
<link href="https://fonts.googleapis.com/css2?family=Arimo:wght@400;700&display=swap" rel="stylesheet">
<style>
  :root {
    --red: #d5161c;
    --ink: #2b2b2b;
    --paper-light: #f4eeee;
    --paper-pink: #e7d3d3;
    --band: #111111;
    --white: #ffffff;
    --skin: #e3b9a3;
    --hand-shadow: #c9a091;
    --glove: #d9d9d9;
    --organ: #c9534a;
  }
  * { margin: 0; padding: 0; box-sizing: border-box; }
  html, body { width: 849px; height: 1200px; overflow: hidden; }
  body { font-family: "Arimo", Arial, sans-serif; }

  .flyer {
    position: relative;
    width: 849px;
    height: 1200px;
    overflow: hidden;
    background: radial-gradient(ellipse at 50% 40%, var(--paper-light) 0%, var(--paper-pink) 100%);
  }

  .brand {
    position: absolute;
    top: 10px;
    left: 14px;
    display: flex;
    align-items: center;
    gap: 8px;
    font-weight: 700;
    font-size: 20px;
    color: var(--ink);
    letter-spacing: 1px;
    z-index: 3;
  }
  .brand-dot {
    width: 22px; height: 22px;
    border-radius: 50%;
    background: var(--red);
  }

  .hands-photo {
    position: absolute;
    top: 0;
    left: 250px;
    width: 599px;
    height: 330px;
    background: radial-gradient(ellipse at 55% 55%, var(--skin) 0%, var(--hand-shadow) 30%, rgba(231,211,211,0) 70%);
  }

  .title {
    position: absolute;
    top: 100px;
    width: 100%;
    text-align: center;
    font-weight: 700;
    font-size: 64px;
    color: var(--red);
    text-shadow: 2px 2px 0 var(--white), -1px -1px 0 var(--white);
    letter-spacing: 0.5px;
    z-index: 3;
  }
  .subtitle {
    position: absolute;
    top: 192px;
    width: 100%;
    text-align: center;
    font-weight: 700;
    font-size: 36px;
    color: var(--red);
    z-index: 3;
  }

  .details {
    position: absolute;
    top: 345px;
    width: 100%;
    text-align: center;
    font-size: 40px;
    color: var(--ink);
    line-height: 72px;
    z-index: 3;
  }

  .events-heading {
    position: absolute;
    top: 618px;
    width: 100%;
    text-align: center;
    font-weight: 700;
    font-size: 44px;
    color: var(--red);
    z-index: 3;
  }
  .events-list {
    position: absolute;
    top: 684px;
    width: 100%;
    text-align: center;
    font-size: 40px;
    color: var(--ink);
    line-height: 78px;
    z-index: 3;
  }

  .stop-hand {
    position: absolute;
    left: 0;
    top: 760px;
    width: 330px;
    height: 440px;
    background: linear-gradient(160deg, var(--glove) 0%, #f2f2f2 50%, var(--red) 100%);
    clip-path: polygon(18% 0, 80% 10%, 100% 40%, 95% 100%, 0 100%, 0 25%);
    opacity: 0.9;
    z-index: 1;
  }

  .colon-illustration {
    position: absolute;
    right: 10px;
    top: 950px;
    width: 140px;
    height: 110px;
    border-radius: 40%;
    background: radial-gradient(circle, #e39a8f 0%, var(--organ) 70%);
    z-index: 1;
  }

  .footer-band {
    position: absolute;
    left: 0;
    bottom: 0;
    width: 849px;
    height: 190px;
    z-index: 0;
  }
  .contact-web {
    position: absolute;
    right: 22px;
    bottom: 22px;
    text-align: right;
    font-size: 30px;
    color: var(--white);
    line-height: 44px;
    z-index: 3;
  }
</style>
</head>
<body>
<main class="flyer">
  <div class="hands-photo" role="img" aria-label="Photo of two hands holding each other"></div>

  <div class="brand"><span class="brand-dot"></span>BRIGHT PATHWAY</div>

  <h1 class="title">BRIGHT PATHWAY,NFP</h1>
  <p class="subtitle">Colon Cancer Fundraiser Fall 2015</p>

  <div class="details">
    <p>Marlow Veterans Hall</p>
    <p>Date - 26th September</p>
    <p>Time-3pm-10pm</p>
  </div>

  <h2 class="events-heading">EVENTS</h2>

  <svg class="footer-band" viewBox="0 0 849 190" aria-hidden="true">
    <path d="M0 80 Q 420 0 849 40 L849 190 L0 190 Z" fill="var(--band)"/>
  </svg>

  <div class="stop-hand" role="img" aria-label="Illustration of a raised gloved hand with a Stop Colon Cancer stamp"></div>
  <div class="colon-illustration" role="img" aria-label="Illustration of the colon"></div>

  <div class="events-list">
    <p>Bean Bag Tournament at 4pm</p>
    <p>Live Band Velvet Orchard at 7pm</p>
    <p>Contact Brenda - 708-555-0193</p>
  </div>

  <div class="contact-web">
    <p>brenda@brightpathwaynfp.org</p>
    <p>www.brightpathwaynfp.org</p>
  </div>
</main>
</body>
</html>
```